依頼詳細
ダンスの発表会は
2年に1回 ホールを借りて発表会を行っています。

今回は2024年 4月14日に開催いたします。
今回で 7回目になります。

発表会の年齢層は 幼稚園から 中学3年生までになります。

発表会のコンセプトは
sub Title: Keep a Warm Glow(意味:輝く笑顔)
Main :Life is fun(意味:全力で楽しむ!)

Keep a Warm Glow は、毎年同じテーマです。
Life is fun はコロナのようにいつ何が起こるかわからないので、今を全力で楽しむという意味をこめて
記載項目
記載内容は下記のとおりです。

*全て 英語で記載
*大文字、小文字に関してはお任せします。

KRN のロゴ

7th

2024.4.14 Sun

1st Open 10:00 Start 10:30
2nd Open 14:30 Start 15:00

Location Toreda Geijutsu Center Hanayuri Hall

Keep a Warm Glow
Life is fun
サイズ
A4
ページ数
片面
希望イメージ
シンプル 複雑
単色 カラフル
暗い 明るい
日常 高級
遊び心 厳粛
未来的 伝統的
女性的 男性的
希望する色
紫系
納品ファイル
• イラストレーター形式 (.ai)
生成AI使用可否
納品物の制作に生成AIの使用がOK
追加で テンプレートページA3 × 3ページ A4 × 1ページ

は別途費用を お支払いいたします。
■ 選んだ理由

最初に希望していた通りのデザインでした。素敵なデザインありがとうございます。

■ 提案者全員のお礼・コメント

本当にたくさんのご提案いただきありがとうございます!
感謝いたします。

```html
<!DOCTYPE html>
<html lang="en">
<head>
<meta charset="UTF-8">
<title>KRN 7th Recital — Keep a Warm Glow</title>
<link rel="stylesheet" href="https://fonts.googleapis.com/css2?family=Poppins:wght@500;600;700;800&display=swap">
<style>
  :root {
    --lilac: #c9b6f2;
    --lavender: #b7a4ee;
    --pink: #f2c4ec;
    --sky: #b9d8f7;
    --violet: #9b86e6;
    --white: #ffffff;
    --yellow: #fff38c;
    --glow: rgba(255, 214, 90, 0.85);
    --soft-shadow: rgba(120, 90, 200, 0.35);
  }
  * { margin: 0; padding: 0; box-sizing: border-box; }
  html, body {
    width: 849px;
    height: 1200px;
    overflow: hidden;
  }
  body {
    font-family: "Poppins", sans-serif;
    background: var(--lilac);
  }
  .poster {
    position: relative;
    width: 849px;
    height: 1200px;
    overflow: hidden;
    color: var(--white);
  }
  .holo-backdrop {
    position: absolute;
    inset: 0;
    background:
      radial-gradient(ellipse 420px 300px at 12% 8%, var(--pink) 0%, transparent 70%),
      radial-gradient(ellipse 380px 460px at 88% 22%, var(--sky) 0%, transparent 70%),
      radial-gradient(ellipse 520px 380px at 30% 55%, var(--violet) 0%, transparent 72%),
      radial-gradient(ellipse 460px 420px at 80% 70%, var(--pink) 0%, transparent 70%),
      radial-gradient(ellipse 500px 360px at 20% 92%, var(--sky) 0%, transparent 70%),
      linear-gradient(160deg, var(--lavender) 0%, var(--lilac) 45%, var(--violet) 100%);
  }
  .tagline {
    position: absolute;
    left: 0;
    width: 100%;
    text-align: center;
    font-weight: 700;
    font-size: 42px;
    line-height: 1.2;
    color: var(--yellow);
    letter-spacing: 0.5px;
    text-shadow: 0 0 10px var(--glow), 0 0 22px var(--glow);
  }
  .tagline--sub { top: 100px; }
  .tagline--main { top: 184px; }
  .event-date {
    position: absolute;
    left: 136px;
    top: 482px;
    font-weight: 700;
    font-size: 33px;
    line-height: 1;
    letter-spacing: 1px;
    white-space: nowrap;
    transform: rotate(-40deg);
    transform-origin: left bottom;
    text-shadow: 0 2px 8px var(--soft-shadow);
  }
  .brand-name {
    position: absolute;
    left: 0;
    width: 100%;
    top: 420px;
    padding-left: 30px;
    text-align: center;
    font-weight: 800;
    font-size: 176px;
    line-height: 1;
    letter-spacing: 6px;
    color: var(--white);
  }
  .edition {
    position: absolute;
    left: 0;
    width: 100%;
    top: 650px;
    text-align: center;
    font-weight: 800;
    font-size: 104px;
    line-height: 1;
    letter-spacing: 4px;
    text-shadow: 0 3px 10px var(--soft-shadow);
  }
  .schedule {
    position: absolute;
    left: 0;
    width: 100%;
    top: 886px;
    list-style: none;
    text-align: center;
    font-weight: 600;
    font-size: 38px;
    line-height: 62px;
    text-shadow: 0 2px 8px var(--soft-shadow);
  }
  .schedule .slot-start { margin-left: 44px; }
  .venue {
    position: absolute;
    left: 0;
    width: 100%;
    top: 1058px;
    text-align: center;
    font-weight: 600;
    font-size: 28px;
    color: var(--yellow);
    text-decoration: underline;
    text-underline-offset: 6px;
    text-decoration-thickness: 2px;
    text-shadow: 0 0 10px var(--glow);
  }
</style>
</head>
<body>
  <main class="poster">
    <div class="holo-backdrop" role="img" aria-label="Holographic lilac, pink and sky-blue swirling gradient background"></div>

    <p class="tagline tagline--sub">Keep a Warm Glow</p>
    <p class="tagline tagline--main">Life is fun</p>

    <p class="event-date">2024.04.14 SUN</p>

    <h1 class="brand-name">KRN</h1>
    <p class="edition">7TH</p>

    <ul class="schedule">
      <li><span class="slot-open">1st Open 10:00</span><span class="slot-start">Start 10:30</span></li>
      <li><span class="slot-open">2nd Open 14:30</span><span class="slot-start">Start 15:00</span></li>
    </ul>

    <p class="venue">Location : Toreda Geijutsu Center Hanayuri Hall</p>
  </main>
</body>
</html>
```